Fundraising Flyer for a School Library

We are a small but fast-growing school in need of funding support for a new Library, Admin and 2 more primary classrooms.
We are hoping that someone can come up with a design for a flyer (A4 - 3 fold) or brochure (2 to an A4) that will encourage people in our community to consider 'partnering' with us to help fund this massive project.
The 'Word' doc attached has some initial wording ideas, however someone with a gift for this type of advertising may well come up with better wording. We're happy for you to use a bit of creativity here.

Target Market(s)

Local businesses, parents and extended families

Industry/Entity Type

School

Requirements
Must have
• Picture of the proposed library.
• Pictures of students from our school.
• You can find information and photos on our school website. http://www.pkrts.example.edu.au/
Should not have
• Anything inappropriate for a Christian School.
• Pictures of random people that aren't from our school - ie, aren't in our school uniform.

```html
<!DOCTYPE html>
<html lang="en">
<head>
<meta charset="utf-8">
<title>Help Us Build a Better Environment – Fundraising Flyer</title>
<link href="https://fonts.googleapis.com/css2?family=Raleway:wght@300;400;500;600;700&display=swap" rel="stylesheet">
<style>
  :root {
    --page-bg: #eef0ee;
    --paper: #ffffff;
    --navy: #1a3f8f;
    --navy-deep: #163a85;
    --blue-band-start: #1a3a86;
    --blue-band-end: #2a66b8;
    --text-grey: #6b6b6b;
    --text-dark: #2c2c2c;
    --rule: #c9c9c9;
    --photo-light: #b9c27e;
    --photo-mid: #8d9a55;
    --photo-shadow: #4f5a30;
    --photo-blue: rgba(96, 140, 190, .55);
  }
  * { box-sizing: border-box; margin: 0; padding: 0; }
  html, body { width: 1200px; height: 900px; overflow: hidden; }
  body {
    background: var(--page-bg);
    font-family: "Raleway", Arial, sans-serif;
    display: flex; align-items: center; justify-content: center;
  }
  .flyer {
    width: 594px; height: 840px;
    background: var(--paper);
    box-shadow: 0 2px 10px rgba(0,0,0,.15);
    display: flex; flex-direction: column;
  }
  .hero {
    position: relative; height: 452px;
    color: #fff; overflow: hidden;
  }
  .hero-photo {
    position: absolute; inset: 0;
    background:
      radial-gradient(ellipse 45% 60% at 78% 55%, var(--photo-blue), transparent 70%),
      linear-gradient(180deg, var(--photo-light) 0%, var(--photo-mid) 50%, var(--photo-shadow) 100%);
  }
  .school-name {
    position: absolute; left: 43px; top: 26px;
    font-size: 15px; line-height: 1.15;
    padding-bottom: 8px; border-bottom: 1px solid rgba(255,255,255,.85);
    width: 218px;
  }
  .school-name strong { font-weight: 700; display: block; }
  .school-name span { font-weight: 400; }
  .headline {
    position: absolute; left: 42px; top: 248px;
    font-size: 53px; font-weight: 500; line-height: 1.16; letter-spacing: -2px;
    text-shadow: 0 1px 3px rgba(0,0,0,.25);
  }
  .details {
    height: 251px; display: flex; padding: 24px 24px 0 43px;
  }
  .column { padding-right: 14px; }
  .column + .column { border-left: 1px solid var(--rule); padding-left: 16px; }
  .col-need { width: 182px; }
  .col-who { width: 146px; }
  .col-how { flex: 1; }
  .column h2 {
    font-size: 15px; font-weight: 400; color: var(--navy); margin-bottom: 16px;
  }
  .column h2 strong { font-weight: 700; }
  .column p, .column li {
    font-size: 10px; font-weight: 300; line-height: 1.3; color: var(--text-grey);
  }
  .column b { font-weight: 600; color: var(--text-dark); }
  .column p + p { margin-top: 3px; }
  .donate-list { list-style: none; margin-top: 2px; }
  .donate-list li::before { content: "• "; }
  .column .account { padding-left: 7px; margin-top: 0; }
  .progress {
    height: 137px; display: flex; align-items: center;
    padding: 0 36px 0 52px; color: #fff;
    background: linear-gradient(90deg, var(--blue-band-start), var(--blue-band-end));
  }
  .progress-text { width: 364px; }
  .progress h3 { font-size: 15px; font-weight: 700; margin-bottom: 9px; }
  .progress h3 span { font-weight: 400; }
  .progress p { font-size: 10px; font-weight: 500; line-height: 1.3; }
  .progress .web { font-weight: 700; font-size: 11px; margin-top: 10px; }
  .band-divider { width: 1px; height: 86px; background: rgba(255,255,255,.7); margin: 0 20px 0 22px; }
  .school-mark {
    width: 98px; height: 98px; border-radius: 50%;
    background: #fff; color: var(--navy-deep);
    display: flex; align-items: center; justify-content: center; text-align: center;
    font-size: 11px; font-weight: 700; line-height: 1.2; padding: 10px;
  }
</style>
</head>
<body>
  <main class="flyer">
    <section class="hero">
      <div class="hero-photo" role="img" aria-label="Photo of a smiling young student in school uniform and bucket hat sitting on a log in a sunny park"></div>
      <div class="school-name"><strong>Parkridge Valley</strong><span>Christian School</span></div>
      <h1 class="headline">Help Us<br>Build a Better<br>Environment.</h1>
    </section>

    <section class="details">
      <div class="column col-need">
        <h2><strong>What</strong> We Need.</h2>
        <p>We are calling for <b>100 Partners</b> to help <b>raise $50,000 or more</b> by tax deductable donations to the PVCS building fund.</p>
        <p>The donations are to cover the costs of the construction of a new <b>Library</b>, <b>Offices</b> and <b>providing 2 additional Primary Class Rooms</b>.</p>
        <p>(The total cost is $1.45m)</p>
      </div>
      <div class="column col-who">
        <h2><strong>Who</strong> Can Help.</h2>
        <p>We are calling for <b>School families</b>, <b>Grandparents</b>, <b>Church memebers</b>, <b>Christian Community</b>, <b>Parkridge Valley Buisnesses</b> and anyone who would like to help.</p>
      </div>
      <div class="column col-how">
        <h2><strong>How</strong> to Help.</h2>
        <p>We are hope to have donations by 30 June with donation amounts of <b>$100</b>, <b>$200</b>, <b>$500</b>, <b>$1000</b>, <b>$2000</b>, <b>$5000</b> or any amount you'd like to donate.</p>
        <p><b>Donate to:</b></p>
        <ul class="donate-list">
          <li>School office directly</li>
          <li>Cheque to PVCS, PO Box 318, Parkridge Heads, NSW, 2450</li>
          <li>Direct deposit to:</li>
        </ul>
        <p class="account">Acc No: XXXXXXXXXXXXXX<br>BSB: XXXXXXX</p>
      </div>
    </section>

    <footer class="progress">
      <div class="progress-text">
        <h3>Progress <span>Reports.</span></h3>
        <p>Number of Partners and progress on money raised will be included in 'The Valley Courier' each week during second term. Individual names will be kept confidential. Business Names will be listed in the end of term Courier and on the School WEB site.</p>
        <p class="web">pkrts.example.edu.au</p>
      </div>
      <div class="band-divider"></div>
      <div class="school-mark">Parkridge Valley</div>
    </footer>
  </main>
</body>
</html>
```